Technical Communications firm needs an article turned into a white paper

We want to redesign a 3-part blog series into a white paper that we can print for a conference. I've consolidated the three posts into the attached Word document.

We are looking for a light, easy to read design. Good use of graphics to support the message. I've added the graphics we used in the original post.

You can view them at
http://www.quillmarrowgroup.com/blog/are-you-satisfied-with-your-dita-solution/

Target Market(s)

Product managers from High-tech, Finance, and Medical industries.

Industry/Entity Type

Information Technology

Colors

Designer to choose colors to be used in the design.

Requirements
Must have
• Must be modern, light, easy to read and slick design. Try to incorporate the graphics provided, but feel free to add more. Must retain the lists and tables.
• Must align with our website/brand.
• Must be easy to read. So not too busy.
• Please move all footnotes to endnotes. You'll need to rework the numbering.
Nice to have
• Awesome coverpage.
Should not have
• Hokey clipart. Not too heavy or hard to read.

```html
<!DOCTYPE html>
<html lang="en">
<head>
<meta charset="utf-8">
<title>Are You Satisfied With Your DITA Solution? – White Paper Spreads</title>
<link rel="stylesheet" href="https://fonts.googleapis.com/css2?family=Bebas+Neue&family=Montserrat:wght@400;600;700&family=Arimo:wght@400&display=swap">
<style>
:root{
  --sheet:#8f8f8f;
  --blue:#1e88e5;
  --blue-deep:#0d5fb3;
  --blue-light:#4fb3f6;
  --ink:#2b2f36;
  --muted:#5d6670;
  --paper:#ffffff;
  --paper-tint:#eef3f8;
}
*{box-sizing:border-box;margin:0;padding:0}
html,body{width:926px;height:1200px;overflow:hidden;background:var(--sheet)}
body{position:relative;font-family:"Montserrat",sans-serif;color:var(--ink)}
.page{position:absolute;width:263px;height:372px;background:linear-gradient(160deg,var(--paper) 40%,var(--paper-tint));box-shadow:0 1px 3px rgba(0,0,0,.35);overflow:hidden}
.caption{position:absolute;width:263px;text-align:center;font:12px "Arimo",sans-serif;color:#111}
.top-band{position:absolute;left:0;top:6px;width:263px;height:14px}
.site-foot{position:absolute;left:0;bottom:12px;width:263px;text-align:center;font-size:4.6px;font-weight:700;color:var(--blue-deep)}
.site-foot::before,.site-foot::after{content:"";position:absolute;top:3px;width:70px;height:1px;background:var(--blue)}
.site-foot::before{left:18px}.site-foot::after{right:18px}
.body-text{position:absolute;left:12px;width:239px;font-size:4.1px;line-height:1.5;color:var(--muted)}
.section-tag{position:absolute;left:12px;padding:1.5px 6px;border:0.7px dashed var(--blue);border-radius:5px;font-size:5px;font-weight:700;color:var(--blue);letter-spacing:.3px}
.byline{position:absolute;left:36px;width:191px;height:18px;background:linear-gradient(var(--blue),var(--blue-deep));color:#fff;text-align:center;font-size:4.1px;font-weight:700;line-height:1.4;padding-top:3px;clip-path:polygon(6% 0,94% 0,100% 50%,94% 100%,6% 100%,0 50%)}
.byline-rule{position:absolute;left:0;width:263px;height:1px;background:var(--blue)}
.numbered{position:absolute;left:0;width:251px;list-style:none}
.numbered li{position:relative;padding-left:28px;font-size:4.1px;line-height:1.5;color:var(--muted)}
.numbered li .num{position:absolute;left:0;top:0;width:20px;height:5px;background:var(--blue);color:#fff;font-size:3.6px;text-align:right;padding-right:3px;line-height:5px;font-weight:700;clip-path:polygon(0 0,100% 0,88% 100%,0 100%)}
.photo{position:absolute;border:1.5px solid var(--blue)}
/* cover */
.cover{background:linear-gradient(180deg,#2196f3 0%,#1a7fdc 45%,#1565c0 100%)}
.brand{position:absolute;left:74px;top:14px;display:flex;align-items:center;gap:6px;color:#fff;font-weight:700;font-size:9px;line-height:1}
.brand-dot{width:30px;height:30px;border-radius:50%;background:#fff}
.cover-title{position:absolute;left:0;top:66px;width:263px;text-align:center;font-family:"Bebas Neue",sans-serif;font-size:31px;line-height:1.02;color:#fff;letter-spacing:.3px}
.cover-pill{position:absolute;left:40px;top:135px;width:183px;height:15px;border:1.5px solid #fff;border-radius:8px;background:#fff;color:var(--blue-deep);font-size:6.8px;font-weight:700;text-align:center;line-height:12px}
.cover-photo{position:absolute;left:0;top:168px;width:263px;height:180px;background:radial-gradient(ellipse at 50% 55%,#dbe9f5 0%,#8fb4d6 40%,#2f5f8c 80%)}
.cover-foot{position:absolute;left:0;bottom:0;width:263px;height:22px;background:var(--blue-deep);color:#fff;text-align:center;font-size:4.6px;font-weight:700;line-height:22px}
/* table */
.compare{position:absolute;left:8px;top:36px;width:247px;height:150px;border:0.7px solid var(--blue)}
.compare-col{position:absolute;top:0;width:123px;padding:16px 7px 0}
.compare-head{position:absolute;top:-6px;left:12px;width:99px;height:11px;background:var(--blue);color:#fff;font-size:5.4px;font-weight:700;text-align:center;line-height:11px}
.compare-col p{font-size:3.9px;line-height:1.4;color:var(--muted);margin-bottom:9px;padding-left:5px;position:relative}
.compare-col p::before{content:"";position:absolute;left:0;top:1.5px;width:2px;height:2px;border-radius:50%;background:var(--blue)}
.endnotes{position:absolute;left:12px;width:239px;font-size:3.1px;line-height:1.45;color:var(--muted)}
.endnotes b{display:block;color:var(--blue);font-size:3.4px;margin-bottom:2px}
.issue-icons{position:absolute;left:16px;top:226px;width:231px;display:flex;justify-content:space-between}
.issue{width:60px;text-align:center;font-size:4px;font-weight:700;color:var(--blue);line-height:1.3}
.issue-ring{width:38px;height:38px;margin:0 auto 5px;border-radius:50%;border:3px solid var(--blue);background:radial-gradient(circle,#fff 45%,#d4e8f9 46%)}
.part-row{position:absolute;left:0;width:251px;font-size:4.1px;line-height:1.5;color:var(--muted);padding-left:34px}
.part-row .tag{position:absolute;left:0;top:0;width:28px;height:5.5px;background:var(--blue);color:#fff;font-size:3.8px;font-weight:700;padding-left:11px;line-height:5.5px}
.part-row em{font-style:normal;color:var(--blue)}
</style>
</head>
<body>

<svg width="0" height="0" style="position:absolute">
  <defs>
    <g id="band">
      <rect x="0" y="6" width="226" height="3" fill="#1e88e5"/>
      <rect x="0" y="10" width="226" height="0.6" fill="#4fb3f6"/>
      <polygon points="218,2 232,2 238,10 224,10" fill="#1e88e5"/>
      <polygon points="234,2 244,2 250,10 240,10" fill="#4fb3f6"/>
      <polygon points="246,2 263,2 263,10 252,10" fill="#0d5fb3"/>
    </g>
  </defs>
</svg>

<!-- Cover -->
<section class="page cover" style="left:34px;top:16px">
  <div class="brand"><span class="brand-dot"></span><span>QUILL MARROW<br>GROUP</span></div>
  <h1 class="cover-title">ARE YOU SATISFIED WITH<br>YOUR DITA SOLUTION?</h1>
  <div class="cover-pill">OUR THREE PART BLOG SERIES CAN HELP</div>
  <div class="cover-photo" role="img" aria-label="Businessman holding a glowing globe with digital devices and people above open hands"></div>
  <div class="cover-foot">www.quillmarrowgroup.com</div>
</section>
<div class="caption" style="left:34px;top:392px">Cover Page</div>

<!-- Page 01 -->
<section class="page" style="left:333px;top:16px">
  <svg class="top-band" viewBox="0 0 263 14"><use href="#band"/></svg>
  <div class="byline-rule" style="top:58px"></div>
  <div class="byline" style="top:50px">BY RORY HALE<br>PRESIDENT OF QUILL MARROW GROUP AUTHORING SOLUTIONS INC.</div>
  <p class="body-text" style="top:84px">If your answer is "No" then you are not alone according to a 2017 survey of more than 250 technical communication professionals conducted by The Docs Drover. The DITA Satisfaction Survey [ i ] indicates that 62% of respondents using DITA are—to varying degrees—dissatisfied. As many as 10% of that group were very dissatisfied reporting that their DITA implementation is experiencing 'big' challenges. It's not surprising that there's significant dissatisfaction amongst those who have adopted DITA. After all, moving to DITA is a seismic shift in technical writing, a big change with many opportunities for things to go wrong.</p>
  <p class="body-text" style="top:139px">The good news is that most DITA users don't see their problems as insurmountable. Many just need a little help getting to where they'd like to be.</p>
  <div class="section-tag" style="top:182px">BREAKDOWN OF THE ISSUES</div>
  <p class="body-text" style="top:206px">The Docs Drover DITA Satisfaction Survey asked respondents to rank the top 10 issues facing DITA users. These issues fit into three major categories including</p>
  <div class="issue-icons">
    <div class="issue"><div class="issue-ring" role="img" aria-label="Head with gears icon"></div>SKILLS<br>DEVELOPMENT</div>
    <div class="issue"><div class="issue-ring" role="img" aria-label="Laptop icon"></div>TECHNOLOGY</div>
    <div class="issue"><div class="issue-ring" role="img" aria-label="Manager with chart icon"></div>MANAGEMENT</div>
  </div>
  <p class="body-text" style="top:320px">The DITA Satisfaction Survey Aggregate Results revealed little spread between the ranking of the issues indicating that respondents likely faced more than one issue of concern.</p>
  <div class="site-foot">www.quillmarrowgroup.com</div>
</section>
<div class="caption" style="left:333px;top:392px">Page 01</div>

<!-- Page 02 -->
<section class="page" style="left:627px;top:16px">
  <svg class="top-band" viewBox="0 0 263 14"><use href="#band"/></svg>
  <div class="section-tag" style="top:34px">IN THIS ARTICLE</div>
  <p class="body-text" style="top:61px">In this article, we examine three issues impacting DITA satisfaction to help you find the best place to start making improvements.</p>
  <div class="part-row" style="top:90px"><span class="tag">Part I</span><em>Skills Development</em> – This problem area is far and away the most pressing obstacle for a successful DITA deployment. Too often authors are left to figure out how to adapt to writing for DITA on their own.</div>
  <div class="part-row" style="top:123px"><span class="tag">Part 2</span><em>Technology</em> – We often hear about the failure of the technology as it relates to performance or complexity. While technology may seem the most likely culprit, it is often not the root cause of the problem.</div>
  <div class="part-row" style="top:157px"><span class="tag">Part 3</span><em>Management</em> – While these issues appear to be of least concern to many survey respondents, they are most likely to form the root cause of all other issues identified in the survey. This points to a general lack of awareness as to the role management should be playing in collaborative, structured authoring solutions.</div>
  <div class="endnotes" style="top:199px"><b>FOOT NOTES</b>[ i ] DITA Satisfaction Survey published by The Docs Drover on May 31, 2017. Listen to an analysis of the results by Rory Hale and guest panelists and download a copy of the results today from TalkStage at www.talkstage.com/webcast/9273/259775</div>
  <div class="photo" role="img" aria-label="Cluster of yellow, red and green road signs pointing in many directions against a cloudy sky" style="left:12px;top:236px;width:240px;height:101px;background:linear-gradient(180deg,#a9c9e6,#e4eef6 60%,#d7c46a 75%,#9aa7b2)"></div>
  <div class="site-foot">www.quillmarrowgroup.com</div>
</section>
<div class="caption" style="left:627px;top:392px">Page 02</div>

<!-- Page 03 -->
<section class="page" style="left:34px;top:411px">
  <svg class="top-band" viewBox="0 0 263 14"><use href="#band"/></svg>
  <div style="position:absolute;left:0;top:30px;width:263px;text-align:center;font-size:8.6px;font-weight:700;color:var(--blue)">PART I: SKILLS DEVELOPMENT</div>
  <div class="byline-rule" style="top:67px"></div>
  <div class="byline" style="top:59px">BY RORY HALE<br>PRESIDENT OF QUILL MARROW GROUP AUTHORING SOLUTIONS INC.</div>
  <p class="body-text" style="top:102px">This article is part of a series based on the results of a survey of more than 250 technical communication professionals conducted by The Docs Drover in 2017 entitled The DITA Satisfaction Survey [ i ]. In the survey, almost two-thirds of respondents voiced concerns with their DITA deployment.</p>
  <p class="body-text" style="top:135px">In our previous article, we introduced the overall results from the survey that pertain to users' dissatisfaction with their DITA solution. In this article, we examine the top rated issues pertaining to skills development.</p>
  <div class="section-tag" style="top:170px">ISSUES RELATED TO SKILLS DEVELOPMENT</div>
  <p class="body-text" style="top:192px">The top ranked reported issues fall under the category of skill development and training. These include</p>
  <ul class="numbered" style="top:213px">
    <li style="margin-bottom:14px"><span class="num">1</span>How do I reuse content? Ranked 1st by 75% of respondents.</li>
    <li style="margin-bottom:14px"><span class="num">2</span>How do I make DITA do what I want it to do? Ranked 2nd by 69% of respondents</li>
    <li style="margin-bottom:14px"><span class="num">3</span>Where can I get DITA training? Ranked 3rd by 64% of respondents.</li>
    <li><span class="num">4</span>How do I create DITA content? Ranked 8th by 56% of respondents.</li>
  </ul>
  <p class="body-text" style="top:292px">This problem area is far and away the most pressing obstacle for a successful DITA deployment. Too often authors are left to figure out how to adapt to writing for DITA on their own. Organizations will normally invest in tools training—and may even opt for a short training course to learn about DITA—but they rarely make the effort to train writers how to author modular, structured topics of content designed for reuse.</p>
  <div class="site-foot">www.quillmarrowgroup.com</div>
</section>
<div class="caption" style="left:34px;top:787px">Page 03</div>

<!-- Page 04 -->
<section class="page" style="left:333px;top:411px">
  <svg class="top-band" viewBox="0 0 263 14"><use href="#band"/></svg>
  <p class="body-text" style="top:32px">It is easy to overlook this training aspect and assume that writers will naturally adapt to this new way of writing. But, those assumptions can lead to big problems.</p>
  <p class="body-text" style="top:57px">In a poll conducted in a recent webinar [ ii ] where half of the participants indicated they were already using DITA, a full 70% indicated that they had no formal DITA training. Of those participants, nearly 60% were self-taught while the others had no training at all. It's no wonder that dissatisfaction is the norm.</p>
  <div class="section-tag" style="top:101px">SELECTING THE BEST TRAINING FOR YOUR NEEDS</div>
  <p class="body-text" style="top:127px">There are many training options available to learn about DITA. Selecting the best training for your team entails examining what it is you need to learn. Most DITA training courses cover the features and walk you through the structures and mechanics of the standard. These courses demonstrate how to markup content, but will often not teach you how to rethink and restructure your content to take advantage of DITA's features. Consider the differences between structured writing and structured markup.</p>
  <div class="photo" role="img" aria-label="Bearded man looking up thoughtfully beside a chalkboard checklist of star ratings" style="left:12px;top:189px;width:240px;height:101px;background:linear-gradient(90deg,#3d4a57,#56636f 60%,#c9a98c 80%,#56636f)"></div>
  <div class="site-foot">www.quillmarrowgroup.com</div>
</section>
<div class="caption" style="left:333px;top:787px">Page 04</div>

<!-- Page 05 -->
<section class="page" style="left:627px;top:411px">
  <svg class="top-band" viewBox="0 0 263 14"><use href="#band"/></svg>
  <div class="compare">
    <div class="compare-col" style="left:0">
      <div class="compare-head">STRUCTURED WRITING</div>
      <p>Coined by Robin Hart in the 1960's as a means of analyzing, organizing, and presenting information optimal for human consumption</p>
      <p>Promotes patterns for format &amp; syntax that become easily recognizable and predictable</p>
      <p>Relies on consistently labelling &amp; chunking information into easily scannable text</p>
      <p>Introduces universal information typing based on intended reader response</p>
    </div>
    <div class="compare-col" style="left:124px">
      <div class="compare-head">STRUCTURED MARKUP</div>
      <p>Allows authors to markup words, phrases, and sections of content for presentation and for meaning for consumption by machines</p>
      <p>Is validated using standard sets of rules that specify consistent and predictable patterns</p>
      <p>Specifies what content goes where but does not limit or restrict how the content is written</p>
      <p>Provides a rich underlying metadata layer for capturing properties related to the content</p>
    </div>
  </div>
  <p class="body-text" style="top:196px">Table reproduced from "Driving Enterprise Productivity from the Front of the DITA XML Train [ iii ]".</p>
  <div class="photo" role="img" aria-label="Man peeking over the bottom of a green chalkboard reading What am I supposed to do" style="left:12px;top:229px;width:240px;height:101px;background:linear-gradient(180deg,#2e7d5b,#1f6a4a)"></div>
  <div class="site-foot">www.quillmarrowgroup.com</div>
</section>
<div class="caption" style="left:627px;top:787px">Page 05</div>

<!-- Page 06 -->
<section class="page" style="left:333px;top:804px">
  <svg class="top-band" viewBox="0 0 263 14"><use href="#band"/></svg>
  <div class="section-tag" style="top:34px">CONTINUOUS COLLABORATIVE LEARNING</div>
  <p class="body-text" style="top:60px">Organizations that wisely invest in comprehensive training for their writing teams also recognize the importance of continuous learning &amp; recurring training. To stay on top of knowledge sharing in your team, consider the following collaboration activities.</p>
  <ul class="numbered" style="top:88px">
    <li style="margin-bottom:10px"><span class="num">1</span>Schedule regular checkpoints where your team discusses what they've learned with other members of the team.</li>
    <li style="margin-bottom:10px"><span class="num">2</span>Assign different members of your team to research and present best practices at regularly scheduled lunch-and-learn sessions.</li>
    <li style="margin-bottom:10px"><span class="num">3</span>Attend webinars and seminars on best practices as a group and then debrief together to discuss aspects that should be incorporated into your day-to-day work.</li>
    <li style="margin-bottom:10px"><span class="num">4</span>Review and update your content standards regularly as a team to keep your procedures and guidelines current &amp; relevant.</li>
    <li><span class="num">5</span>Pair up senior members of your team with new or junior members for regular mentoring and coaching.</li>
  </ul>
  <div class="section-tag" style="top:217px">QUILL MARROW GROUP STRUCTURED AUTHOR TRAINING</div>
  <p class="body-text" style="top:242px">Quill Marrow Group has many years of experience teaching organizations how to write better structured content. Our inhouse, instructor-led training courses run from 1 to 5 days depending on your needs and cover the gamut of tools and techniques needed for successful structured authoring. Learn more about our DITA training. Or contact Quill Marrow Group to find out more about how we can address your specific training needs.</p>
  <div class="endnotes" style="top:290px"><b>FOOT NOTES</b>
    [ i ] DITA Satisfaction Survey published by The Docs Drover on May 31, 2017. Listen to an analysis of the results by Rory Hale and guest panelists and download a copy of the results today from TalkStage at www.talkstage.com/webcast/9273/259775<br><br>
    [ ii ] The Cognitive Science Behind Intelligent Content presented by Rory Hale on July 21, 2016. See www.talkstage.com/webcast/9273/214245 for details.<br><br>
    [ iii ] Driving Enterprise Productivity from the Front of the DITA XML Train presented by Rory Hale and Dale Garner at the Structured Docs Summit in Lakeport.
  </div>
  <div class="site-foot">www.quillmarrowgroup.com</div>
</section>
<div class="caption" style="left:333px;top:1179px">Page 06</div>

</body>
</html>
```